Technical audit needs a report template

As our company runs various technical audits, we also provide findings on paper, online or in Powerpoint. For this reason we need an identity pack, which includes business cards, complimentary cards, letterhead and the likes.

Who would be up to create this stationery pack for us? We hope to receive a style for these documents, that look professional and can be easily extended.
Updates

Project Deadline Extended Reason: I would like to provide the opportunity to friended designers to submit their designs too! Added Sunday, October 9, 2016

Target Market(s)

Start-ups, scale-ups and investors

Industry/Entity Type

Investment

Contact Information for Business Card

Street: Kleverhoekslaan 42
Postcode: 3614KM
City: Utrecht
Country: The Netherlands
Phone: +31 305819364
Cell Phone: +31 6 57192830
email: jeroen@veldmarkcheck.example
website: https://veldmarkcheck.example

Requirements
Must have
• I don't have inspiration, should just be a slick design based on the logo provided.
Nice to have
• Logo could be on the back of the card?
Should not have
• Should not use different colours then the logo, or at least fit the colour scheme.

```html
<!DOCTYPE html>
<html lang="en">
<head>
<meta charset="utf-8">
<title>Veldmark Check – Stationery</title>
<link href="https://fonts.googleapis.com/css2?family=Open+Sans:wght@400;600;700&display=swap" rel="stylesheet">
<style>
  :root {
    --bg: #e4e5e7;
    --paper: #ffffff;
    --ink: #3d4650;
    --ink-soft: #6b747d;
    --brand: #2a93c9;
    --brand-light: #a9dcef;
    --brand-pale: #e6f5fb;
    --card-back: #72bbdf;
    --card-back-deep: #4fa8d6;
    --rule: #c9ccd0;
  }
  * { box-sizing: border-box; margin: 0; padding: 0; }
  html, body { width: 1200px; height: 874px; overflow: hidden; }
  body {
    background: var(--bg);
    font-family: "Open Sans", Arial, sans-serif;
    color: var(--ink);
    position: relative;
  }
  .sheet { position: absolute; background: var(--paper); overflow: hidden; box-shadow: 0 4px 14px rgba(0,0,0,.18); }
  .brand { display: flex; align-items: center; gap: 5px; position: absolute; }
  .brand-mark { width: 14px; height: 14px; background: var(--brand); }
  .brand-name { font-weight: 700; color: var(--ink); font-size: 13px; letter-spacing: .3px; text-transform: uppercase; }
  .backdrop { position: absolute; }

  /* Letterhead */
  .letterhead { left: 75px; top: 127px; width: 447px; height: 658px; }
  .letterhead .backdrop { left: 0; right: 0; bottom: 0; height: 300px;
    background: linear-gradient(180deg, rgba(230,245,251,0) 0%, var(--brand-pale) 45%, #d3eef8 100%); }
  .letterhead .brand { left: 56px; top: 14px; }
  .sender-address { position: absolute; right: 22px; top: 14px; text-align: right; font-size: 6px; line-height: 1.55; color: var(--ink-soft); }
  .letter-rule { position: absolute; left: 56px; right: 22px; top: 85px; height: 1px; background: var(--rule); }
  .recipient { position: absolute; left: 56px; top: 126px; font-size: 6.5px; line-height: 2; color: var(--ink); }
  .letter-body { position: absolute; left: 56px; right: 44px; top: 240px; font-size: 7px; line-height: 1.9; color: var(--ink); }
  .letter-body p { margin-bottom: 4px; }
  .signature { margin-top: 8px; }
  .signature-name { margin-top: 16px; }

  /* Business card front */
  .card-front { left: 609px; top: 112px; width: 274px; height: 155px; }
  .card-front .backdrop { right: 0; top: 0; bottom: 0; width: 190px;
    background: linear-gradient(120deg, rgba(169,220,239,0) 0%, rgba(169,220,239,.55) 60%, var(--brand-light) 100%); }
  .card-front .brand { left: 14px; top: 12px; }
  .card-front .brand-name { font-size: 10px; }
  .card-front .brand-mark { width: 11px; height: 11px; }
  .holder { position: absolute; right: 18px; top: 74px; text-align: right; }
  .holder-name { font-size: 8.5px; font-weight: 600; letter-spacing: .6px; text-transform: uppercase; }
  .holder-role { font-size: 5px; color: var(--ink-soft); margin-top: 1px; }
  .contact-list { position: absolute; right: 18px; top: 109px; list-style: none; font-size: 6px; line-height: 1.6; text-align: right; color: var(--ink); }
  .contact-list li::after { content: ""; display: inline-block; width: 4px; height: 4px; background: var(--brand); margin-left: 6px; vertical-align: 1px; }

  /* Business card back */
  .card-back { left: 803px; top: 225px; width: 274px; height: 156px; background: var(--card-back); }
  .card-back .backdrop { inset: 0;
    background: linear-gradient(135deg, var(--card-back) 0%, var(--card-back-deep) 55%, var(--card-back) 100%); }
  .card-back .brand { left: 172px; top: 114px; }
  .card-back .brand-mark { background: #ffffff; opacity: .75; }
  .card-back .brand-name { color: #e9f6fc; font-size: 12px; }

  /* Envelope */
  .envelope { left: 609px; top: 440px; width: 544px; height: 244px; }
  .envelope-flap { position: absolute; left: 0; right: 0; top: 0; height: 24px; background: var(--card-back-deep); }
  .envelope .backdrop { left: 0; top: 24px; bottom: 0; width: 300px;
    background: linear-gradient(90deg, var(--brand-pale) 0%, rgba(230,245,251,.5) 70%, rgba(230,245,251,0) 100%); }
  .envelope .brand.sender { left: 25px; top: 54px; }
  .envelope .brand.feature { left: 300px; top: 82px; gap: 10px; }
  .envelope .brand.feature .brand-mark { width: 40px; height: 40px; background: #d6e6ee; }
  .envelope .brand.feature .brand-name { font-size: 32px; color: #d6e6ee; font-weight: 700; }
  .envelope-address { position: absolute; left: 388px; top: 200px; font-size: 6.5px; line-height: 1.55; color: var(--ink-soft); }
</style>
</head>
<body>

<section class="sheet letterhead">
  <div class="backdrop" role="img" aria-label="Soft blue background band"></div>
  <div class="brand"><span class="brand-mark"></span><span class="brand-name">Veldmark Check</span></div>
  <address class="sender-address">Kleverhoekslaan 42 Utrecht<br>3614KM The Netherlands<br>+31 305819364</address>
  <div class="letter-rule"></div>
  <div class="recipient">
    Lotte Brink<br>Title<br>Company Name<br>4321 First Street<br>Anytown, State ZIP<br>Date 9/30/12
  </div>
  <div class="letter-body">
    <p>Dear Lotte,</p>
    <p>Thank you for meeting with our team last week. This letter summarises the scope of the technical audit we agreed on, the planned schedule and the people involved on both sides.</p>
    <p>Our auditors will review the architecture, the code base and the deployment process, and will interview key staff. Findings are shared in a written report and a short presentation.</p>
    <p>Please let us know if any dates need to change. We look forward to working with you.</p>
    <p class="signature">Sincerely yours,</p>
    <p class="signature-name">Name Here</p>
  </div>
</section>

<section class="sheet card-back">
  <div class="backdrop" role="img" aria-label="Blue gradient card back"></div>
  <div class="brand"><span class="brand-mark"></span><span class="brand-name">Veldmark Check</span></div>
</section>

<section class="sheet card-front">
  <div class="backdrop" role="img" aria-label="Soft blue background band"></div>
  <div class="brand"><span class="brand-mark"></span><span class="brand-name">Veldmark Check</span></div>
  <div class="holder">
    <div class="holder-name">Daan V. Hollander</div>
    <div class="holder-role">Chief Financial Officer</div>
  </div>
  <ul class="contact-list">
    <li>+31 305819364</li>
    <li>www.veldmarkcheck.example</li>
    <li>info@veldmarkcheck.example</li>
  </ul>
</section>

<section class="sheet envelope">
  <div class="envelope-flap"></div>
  <div class="backdrop" role="img" aria-label="Soft blue background band"></div>
  <div class="brand sender"><span class="brand-mark"></span><span class="brand-name">Veldmark Check</span></div>
  <div class="brand feature"><span class="brand-mark"></span><span class="brand-name">Veldmark Check</span></div>
  <address class="envelope-address">Kleverhoekslaan 42 Utrecht<br>3614KM The Netherlands</address>
</section>

</body>
</html>
```